Vehicle branding of 2009 valmorant 3500 Tessory Cargo Van

A unique, creative, innovative vehicle branding design that will turn heads. It must be unforgettable. Find attached my logo, examples of creative designs and pictures of my bus. The company is into drycleaning, laundry, professional tailoring repairs and alterations, industrial cleaning. We also offer free pick up and delivery. The numbers on the bus should be 08137264018, 08072613845. email: foldnfreshcleaners@postvale.com.
Updates

Industry/Entity Type

Cargo

Requirements
Must have
• Logo, Phone number, email address, free pick up and delivery, what we do(drycleaning, laundry,tailor repairs and alterations, industrial cleaning)
Nice to have
• surprise me

```html
<!DOCTYPE html>
<html lang="en">
<head>
<meta charset="utf-8">
<title>Fold 'n Fresh Cleaners – Van Wrap</title>
<link href="https://fonts.googleapis.com/css2?family=Roboto+Condensed:wght@400;700&family=Patrick+Hand&display=swap" rel="stylesheet">
<style>
  :root{
    --canvas:#ffffff;
    --body-light:#eef7fc;
    --body-mid:#d4ebf7;
    --brand-blue:#1f6fd1;
    --deep-blue:#0f4fa8;
    --water:#3aa0e8;
    --water-light:#bfe3fa;
    --trim:#1d1f22;
    --glass:#c9d7df;
    --lamp:#b3202a;
    --text-dark:#1a2a5c;
  }
  html,body{margin:0;padding:0;overflow:hidden;background:var(--canvas);}
  .wrap-sheet{width:1200px;height:982px;position:relative;overflow:hidden;}
  .wrap-sheet svg{display:block;}
  .brand-name{font-family:"Roboto Condensed",sans-serif;font-weight:700;fill:var(--deep-blue);}
  .headline{font-family:"Roboto Condensed",sans-serif;font-weight:700;fill:var(--brand-blue);}
  .contact{font-family:"Roboto Condensed",sans-serif;font-weight:700;fill:var(--text-dark);}
  .services{font-family:"Patrick Hand",cursive;fill:var(--brand-blue);}
  .tag-text{font-family:"Roboto Condensed",sans-serif;font-weight:700;fill:#ffffff;}
</style>
</head>
<body>
<div class="wrap-sheet">
<svg width="1200" height="982" viewBox="0 0 1200 982" xmlns="http://www.w3.org/2000/svg">
  <defs>
    <linearGradient id="bodyFill" x1="0" y1="0" x2="0" y2="1">
      <stop offset="0" stop-color="#ffffff"/>
      <stop offset="1" stop-color="#d9eef9"/>
    </linearGradient>
    <linearGradient id="waterFill" x1="0" y1="0" x2="0" y2="1">
      <stop offset="0" stop-color="#bfe3fa" stop-opacity="0"/>
      <stop offset=".45" stop-color="#7cc4f2"/>
      <stop offset="1" stop-color="#1f6fd1"/>
    </linearGradient>
    <linearGradient id="rearWaterFill" x1="0" y1="0" x2="1" y2="1">
      <stop offset="0" stop-color="#bfe3fa" stop-opacity="0"/>
      <stop offset=".35" stop-color="#bfe3fa" stop-opacity=".5"/>
      <stop offset=".7" stop-color="#7cc4f2"/>
      <stop offset="1" stop-color="#1f6fd1"/>
    </linearGradient>
    <linearGradient id="roomFill" x1="0" y1="0" x2="0" y2="1">
      <stop offset="0" stop-color="#e9eef2"/>
      <stop offset=".55" stop-color="#c8c3cf"/>
      <stop offset="1" stop-color="#dfe3e7"/>
    </linearGradient>
  </defs>

  <!-- ===== Side elevation ===== -->
  <g class="van-side">
    <path d="M226,215 L322,165 L368,104 Q378,92 400,92 L836,92 Q852,92 853,112 L858,300 L226,300 Z" fill="url(#bodyFill)" stroke="#b9c6cf"/>
    <path d="M366,112 L470,112 L470,178 L336,178 Z" fill="var(--glass)"/>
    <rect x="218" y="258" width="20" height="30" rx="3" fill="var(--trim)"/>
    <rect x="230" y="232" width="10" height="14" fill="#e59b2a"/>
    <rect x="840" y="258" width="22" height="26" rx="3" fill="var(--trim)"/>
    <rect x="236" y="258" width="250" height="44" fill="url(#waterFill)" role="img" aria-label="Blue water splash with bubbles"/>
    <rect x="646" y="160" width="208" height="142" fill="url(#waterFill)" role="img" aria-label="Blue water splash with bubbles"/>
    <rect x="832" y="125" width="14" height="42" fill="var(--lamp)"/>
    <rect x="488" y="98" width="158" height="190" fill="url(#roomFill)" role="img" aria-label="Laundry room with hanging clothes and two front-loading washing machines"/>
    <line x1="488" y1="98" x2="488" y2="300" stroke="#aab6be"/>
    <line x1="646" y1="98" x2="646" y2="300" stroke="#aab6be"/>
    <path d="M270,300 A60,60 0 0 1 390,300 Z" fill="var(--trim)"/>
    <path d="M674,300 A60,60 0 0 1 794,300 Z" fill="var(--trim)"/>
    <circle cx="330" cy="295" r="40" fill="var(--trim)"/>
    <circle cx="330" cy="295" r="22" fill="#9aa3aa"/>
    <circle cx="734" cy="295" r="40" fill="var(--trim)"/>
    <circle cx="734" cy="295" r="22" fill="#9aa3aa"/>

    <g class="logo-lockup">
      <circle cx="414" cy="203" r="10" fill="var(--brand-blue)"/>
      <text class="brand-name" x="430" y="238" font-size="19" text-anchor="middle">Fold 'n Fresh</text>
      <text class="brand-name" x="430" y="248" font-size="7" text-anchor="middle" letter-spacing="2">CLEANERS</text>
    </g>

    <text class="services" font-size="10.5" text-anchor="middle">
      <tspan x="732" y="112">Drycleaning, Laundry, Professional Tailoring repairs</tspan>
      <tspan x="732" y="126">and alterations, Industrial cleaning</tspan>
    </text>
    <g transform="translate(650,133) rotate(18)">
      <path d="M0,8 L48,0 L50,26 L2,34 L-8,20 Z" fill="var(--brand-blue)"/>
      <text class="tag-text" x="6" y="15" font-size="6">We also offer free pick</text>
      <text class="tag-text" x="8" y="24" font-size="6">up and delivery.</text>
    </g>
    <g class="contact-side">
      <circle cx="711" cy="143" r="4.5" fill="none" stroke="var(--deep-blue)" stroke-width="1.3"/>
      <text class="contact" x="719" y="147" font-size="9" textLength="104" lengthAdjust="spacingAndGlyphs">08137264018, 08072613845</text>
      <rect x="706" y="153" width="9" height="6" fill="var(--deep-blue)"/>
      <text class="contact" x="719" y="160" font-size="8" textLength="104" lengthAdjust="spacingAndGlyphs">foldnfreshcleaners@postvale.com</text>
    </g>
  </g>

  <!-- ===== Rear elevation ===== -->
  <g class="van-rear">
    <path d="M410,400 Q410,372 440,372 L720,372 Q748,372 750,400 L762,655 L392,655 Z" fill="url(#bodyFill)" stroke="#b9c6cf"/>
    <rect x="396" y="440" width="20" height="62" rx="4" fill="var(--lamp)"/>
    <rect x="744" y="440" width="20" height="62" rx="4" fill="var(--lamp)"/>
    <path d="M548,655 L548,560 Q640,520 757,540 L762,655 Z" fill="url(#rearWaterFill)" role="img" aria-label="Blue water splash with bubbles"/>
    <line x1="575" y1="380" x2="575" y2="655" stroke="#aab6be"/>
    <rect x="566" y="548" width="90" height="44" rx="4" fill="var(--trim)"/>

    <rect x="424" y="388" width="138" height="115" rx="8" fill="#e4f2fa" stroke="#8f9aa2"/>
    <rect x="587" y="388" width="138" height="115" rx="8" fill="#ffffff" stroke="#8f9aa2"/>

    <g class="logo-lockup">
      <circle cx="493" cy="422" r="14" fill="var(--brand-blue)"/>
      <text class="brand-name" x="493" y="478" font-size="24" text-anchor="middle">Fold 'n Fresh</text>
      <text class="brand-name" x="493" y="490" font-size="8" text-anchor="middle" letter-spacing="3">CLEANERS</text>
    </g>

    <g class="values">
      <path d="M592,431 l5,-6 l5,6 z" fill="var(--brand-blue)"/>
      <text class="headline" x="606" y="437" font-size="20">Professional</text>
      <path d="M592,454 l5,-6 l5,6 z" fill="var(--brand-blue)"/>
      <text class="headline" x="606" y="460" font-size="20">Reliable</text>
      <path d="M592,477 l5,-6 l5,6 z" fill="var(--brand-blue)"/>
      <text class="headline" x="606" y="483" font-size="20">Affordable</text>
    </g>

    <g class="contact-rear">
      <circle cx="549" cy="520" r="6" fill="none" stroke="var(--deep-blue)" stroke-width="1.6"/>
      <text class="contact" x="560" y="525" font-size="13">08137264018, 08072613845</text>
      <rect x="543" y="534" width="12" height="8" fill="var(--deep-blue)"/>
      <text class="contact" x="560" y="543" font-size="11">foldnfreshcleaners@postvale.com</text>
    </g>

    <rect x="438" y="510" width="34" height="36" rx="4" fill="#6b7078" role="img" aria-label="Laundry basket illustration"/>
    <g transform="translate(436,568) rotate(-14)">
      <rect x="0" y="-18" width="96" height="40" fill="var(--brand-blue)"/>
      <text class="tag-text" x="48" y="-2" font-size="10" text-anchor="middle">We also offer free pick</text>
      <text class="tag-text" x="48" y="12" font-size="10" text-anchor="middle">up and delivery.</text>
    </g>
    <rect x="452" y="588" width="90" height="60" rx="6" fill="#e96d22" role="img" aria-label="Stack of folded colourful towels"/>

    <rect x="388" y="655" width="378" height="48" rx="8" fill="var(--trim)"/>
    <rect x="400" y="700" width="44" height="58" rx="8" fill="var(--trim)"/>
    <rect x="710" y="700" width="44" height="58" rx="8" fill="var(--trim)"/>
  </g>
</svg>
</div>
</body>
</html>
```